Killer business card for bowling event and marketing company

Rapid 'Q' Promotions is a sports marketing company that specializes in unique bowling events that provide return on investment for sponsors and memorable experiences for participants and spectators. We need a new business card that simultaneously communicates professionalism and fun. Our preferred colors are black and re

Target Market(s)

Executives in the marketing and sponsorship departments of companies, tourism executives, bowling center owners, and people who love to bowl.

Industry/Entity Type

Business

Contact Information for Business Card

Dean T Walsh
Rapid 'Q' Promotions
PO Box 47
Fernvale, Oregon USA 22871
Email: deant@rapidqpromotions.com
Mobile: 1-555-518-3762

Requirements
Must have
• Our preferred colors are black and red.
Nice to have
• I am considering the use of the attached image for the back of the card.

```html
<!DOCTYPE html>
<html lang="en">
<head>
<meta charset="utf-8">
<title>Rapid 'Q' Promotions – Business Card</title>
<link href="https://fonts.googleapis.com/css2?family=Montserrat:wght@700;800&family=Arimo:wght@400;700&family=Noto+Serif:ital@1&display=swap" rel="stylesheet">
<style>
  :root {
    --page: #8d8d8d;
    --card-black: #141112;
    --photo-dark: #2a1b1b;
    --photo-warm: #4a2a22;
    --red: #c8141a;
    --red-deep: #a50f14;
    --white: #ffffff;
  }
  html, body {
    margin: 0;
    width: 1200px;
    height: 967px;
    overflow: hidden;
    background: var(--page);
  }
  .sheet {
    position: relative;
    width: 1200px;
    height: 967px;
  }
  .card {
    position: absolute;
    left: 210px;
    width: 780px;
    height: 446px;
    background: var(--card-black);
    overflow: hidden;
    box-shadow: 0 6px 18px rgba(0,0,0,.35);
  }
  .card--back { top: 22px; }
  .card--front { top: 499px; }

  .card__photo {
    position: absolute;
    inset: 0;
    background:
      radial-gradient(ellipse at 30% 70%, rgba(120,60,40,.45), transparent 60%),
      radial-gradient(ellipse at 80% 40%, rgba(90,40,35,.4), transparent 55%),
      linear-gradient(160deg, var(--photo-dark), #120d0e 55%, var(--photo-warm));
  }
  .card__band {
    position: absolute;
    top: 0;
    bottom: 0;
    background: var(--red);
    display: flex;
    flex-direction: column;
    align-items: center;
    justify-content: center;
    gap: 22px;
  }
  .card--back .card__band { left: 45%; width: 30%; }
  .card--front .card__band { left: 57%; width: 30%; }

  .brand__dot {
    width: 110px;
    height: 110px;
    border-radius: 50%;
    background: var(--card-black);
  }
  .brand__name {
    font-family: "Montserrat", sans-serif;
    font-weight: 800;
    color: var(--white);
    font-size: 24px;
    line-height: 1.15;
    text-align: center;
    letter-spacing: .5px;
    margin: 0;
  }

  .contact {
    position: absolute;
    left: 34px;
    top: 30px;
    width: 380px;
    color: var(--white);
  }
  .contact__name {
    font-family: "Montserrat", sans-serif;
    font-weight: 800;
    font-size: 38px;
    margin: 0;
    line-height: 1;
    letter-spacing: .5px;
  }
  .contact__company {
    font-family: "Arimo", sans-serif;
    font-weight: 700;
    font-size: 22px;
    margin: 4px 0 0;
    letter-spacing: .5px;
  }
  .contact__company .accent { color: var(--red); }
  .contact__rule {
    height: 2px;
    background: var(--red-deep);
    margin: 8px 0 22px;
    width: 370px;
  }
  .contact__list {
    list-style: none;
    margin: 0;
    padding: 0;
    display: flex;
    flex-direction: column;
    gap: 20px;
  }
  .contact__item {
    display: flex;
    align-items: flex-start;
    gap: 14px;
    font-family: "Arimo", sans-serif;
    font-size: 18px;
  }
  .contact__icon {
    flex: none;
    width: 34px;
    height: 34px;
    border-radius: 7px;
    background: var(--red);
    display: flex;
    align-items: center;
    justify-content: center;
  }
  .contact__text { padding-top: 7px; }
  .contact__text--phone { font-family: "Noto Serif", serif; font-style: italic; font-size: 19px; }
  .contact__text--address {
    font-weight: 700;
    text-transform: uppercase;
    line-height: 1.2;
    padding-top: 4px;
    text-align: right;
  }
  .contact__text--address span { display: block; }
</style>
</head>
<body>
<main class="sheet">

  <section class="card card--back" aria-label="Card back">
    <div class="card__photo" role="img" aria-label="Darkened photo of a bowler on a bowling lane"></div>
    <div class="card__band">
      <div class="brand__dot"></div>
      <p class="brand__name">RAPID 'Q'<br>PROMOTIONS</p>
    </div>
  </section>

  <section class="card card--front" aria-label="Card front">
    <div class="card__photo" role="img" aria-label="Darkened photo of bowling pins at the end of a lane"></div>
    <div class="contact">
      <h1 class="contact__name">DEAN T WALSH</h1>
      <p class="contact__company">RAPID <span class="accent">'Q'</span> PROMOTIONS</p>
      <div class="contact__rule"></div>
      <ul class="contact__list">
        <li class="contact__item">
          <span class="contact__icon">
            <svg width="18" height="18" viewBox="0 0 24 24" aria-hidden="true"><path fill="#fff" d="M6.6 10.8a15 15 0 0 0 6.6 6.6l2.2-2.2c.3-.3.7-.4 1-.2 1.1.4 2.3.6 3.6.6.6 0 1 .4 1 1V20c0 .6-.4 1-1 1A17 17 0 0 1 3 4c0-.6.4-1 1-1h3.5c.6 0 1 .4 1 1 0 1.3.2 2.5.6 3.6.1.3 0 .7-.2 1z"/></svg>
          </span>
          <span class="contact__text contact__text--phone">1-555-518-3762</span>
        </li>
        <li class="contact__item">
          <span class="contact__icon">
            <svg width="20" height="16" viewBox="0 0 20 16" aria-hidden="true"><rect x="1" y="1" width="18" height="14" fill="none" stroke="#fff" stroke-width="2"/><path d="M1 1l9 7 9-7" fill="none" stroke="#fff" stroke-width="2"/></svg>
          </span>
          <span class="contact__text">deant@rapidqpromotions.com</span>
        </li>
        <li class="contact__item">
          <span class="contact__icon">
            <svg width="16" height="20" viewBox="0 0 16 20" aria-hidden="true"><path fill="#fff" d="M8 0a7 7 0 0 0-7 7c0 5 7 13 7 13s7-8 7-13a7 7 0 0 0-7-7zm0 9.5A2.5 2.5 0 1 1 8 4.5a2.5 2.5 0 0 1 0 5z"/></svg>
          </span>
          <span class="contact__text contact__text--address">Fernvale, Oregon<span>USA 22871</span></span>
        </li>
      </ul>
    </div>
    <div class="card__band">
      <div class="brand__dot"></div>
      <p class="brand__name">RAPID 'Q'<br>PROMOTIONS</p>
    </div>
  </section>

</main>
</body>
</html>
```